Educational non-profit needs an End of the Year Flyer

We need a flyer to mail to our supporters asking for donations to our program. Crestwood Lantern Youth House runs after school programs for low-income students in Pasadena, CA. This is our end of the year mailing to supporters asking them to finish out the year with their contributions so that we can meet our budget.

Target Market(s)

Donors and supporters of organization

Industry/Entity Type

Non-Profit

Font styles to use
Serif

Colors

Designer to choose colors to be used in the design.

Requirements
Must have
• The project should fit on a 6x9" card, and be printed on front and back. It should show pictures, use the copy I have included, a space for a label address, a stamp, and the return address.
Nice to have
• eye-catching, fun

```html
<!DOCTYPE html>
<html lang="en">
<head>
<meta charset="utf-8">
<title>Crestwood Lantern Youth House – End of Year Flyer</title>
<link href="https://fonts.googleapis.com/css2?family=Noto+Serif:wght@300;400&family=Open+Sans:wght@400&display=swap" rel="stylesheet">
<style>
  :root{
    --board:#0b1a21;
    --paper:#f1f1f1;
    --paper-back:#ffffff;
    --ink:#3a3a3a;
    --ink-soft:#6b6b6b;
    --olive:#c4c46a;
    --rule:#c9c9c9;
    --label:#ffffff;
  }
  *{margin:0;padding:0;box-sizing:border-box}
  html,body{width:1200px;height:1200px;overflow:hidden;background:var(--board)}
  .board{position:relative;width:1200px;height:1200px;background:var(--board)}
  .card{position:absolute;top:224px;width:479px;height:719px;overflow:hidden}
  .card--front{left:114px;background:var(--paper)}
  .card--back{left:607px;background:var(--paper-back)}

  .org-mark{position:absolute;left:18px;top:24px;width:72px;text-align:center;
    font-family:"Noto Serif",serif;font-weight:400;font-size:8px;line-height:1.2;color:var(--ink)}
  .org-mark__dot{display:block;width:40px;height:40px;margin:0 auto 6px;border-radius:50%;background:var(--olive)}

  .front-title{position:absolute;left:92px;right:20px;top:54px;text-align:center;
    font-family:"Noto Serif",serif;font-weight:400;font-size:24px;line-height:27px;color:var(--ink);letter-spacing:.3px}

  .photo-art{position:absolute;left:0;top:0}

  .mission{position:absolute;left:0;right:0;top:546px;text-align:center;
    font-family:"Noto Serif",serif;font-weight:400;font-size:13.3px;line-height:19px;color:var(--ink);text-transform:uppercase;letter-spacing:.2px}

  .contact-row{position:absolute;left:18px;right:18px;top:682px;display:flex;justify-content:space-between;align-items:center;
    font-family:"Noto Serif",serif;font-weight:300;font-size:10px;color:var(--ink)}
  .contact-item{display:flex;align-items:center;gap:4px;white-space:nowrap}
  .contact-icon{width:14px;height:14px;flex:none}

  .stamp-box{position:absolute;right:22px;top:22px;width:48px;height:58px;border:1px dashed var(--rule)}

  .appeal{position:absolute;left:108px;top:163px;width:272px;
    font-family:"Noto Serif",serif;font-weight:300;font-size:10.6px;line-height:13.4px;color:var(--ink-soft)}
  .appeal p{margin-bottom:13.4px}

  .return-address{position:absolute;right:108px;top:507px;text-align:right;font-style:normal;
    font-family:"Noto Serif",serif;font-weight:300;font-size:9.4px;line-height:11.2px;color:var(--ink)}

  .label-space{position:absolute;left:108px;top:590px;width:263px;height:84px;border:1px dashed var(--rule)}

  .side-label{position:absolute;top:978px;font-family:"Open Sans",sans-serif;font-size:18px;color:var(--label);transform:translateX(-50%)}
</style>
</head>
<body>
<main class="board">

  <section class="card card--front">
    <div class="org-mark"><span class="org-mark__dot"></span>Crestwood Lantern Youth House</div>
    <h1 class="front-title">CRESTWOOD LANTERN<br>YOUTH HOUSE</h1>

    <svg class="photo-art" width="479" height="719" viewBox="0 0 479 719">
      <defs>
        <linearGradient id="eventGrad" x1="0" y1="0" x2="0" y2="1">
          <stop offset="0" stop-color="#0e0e0e"/>
          <stop offset=".4" stop-color="#2a2320"/>
          <stop offset=".62" stop-color="#8a3a36"/>
          <stop offset=".82" stop-color="#4a4a5a"/>
          <stop offset="1" stop-color="#b08a64"/>
        </linearGradient>
        <linearGradient id="parkGrad" x1="0" y1="0" x2="0" y2="1">
          <stop offset="0" stop-color="#6f8a62"/>
          <stop offset=".45" stop-color="#b49a8c"/>
          <stop offset="1" stop-color="#2e2c36"/>
        </linearGradient>
        <linearGradient id="gymGrad" x1="0" y1="0" x2="0" y2="1">
          <stop offset="0" stop-color="#d0ad82"/>
          <stop offset=".5" stop-color="#8c6a5c"/>
          <stop offset="1" stop-color="#2f2a36"/>
        </linearGradient>
        <linearGradient id="playGrad" x1="0" y1="0" x2="0" y2="1">
          <stop offset="0" stop-color="#cbb9a2"/>
          <stop offset="1" stop-color="#7e6c5e"/>
        </linearGradient>
      </defs>
      <g role="img" aria-label="Photo of children at a park playground">
        <circle cx="382" cy="214" r="72" fill="url(#parkGrad)" stroke="var(--olive)" stroke-width="5"/>
      </g>
      <g role="img" aria-label="Photo of girls holding basketballs in a gym">
        <circle cx="245" cy="286" r="73" fill="url(#gymGrad)" stroke="var(--olive)" stroke-width="5"/>
      </g>
      <g role="img" aria-label="Photo of a smiling child on a playground swing">
        <circle cx="96" cy="354" r="72" fill="url(#playGrad)" stroke="var(--olive)" stroke-width="5"/>
      </g>
      <path role="img" aria-label="Photo of a large group of children at a holiday concert on stage"
        d="M0 363 C120 355 250 330 340 290 C410 258 455 215 479 177 L479 519 L0 519 Z"
        fill="url(#eventGrad)"/>
    </svg>

    <p class="mission">Crestwood Lantern Youth House provides<br>educational and enrichment programs for at-risk<br>children, youth and families in Pasadena, California</p>

    <div class="contact-row">
      <span class="contact-item">
        <svg class="contact-icon" viewBox="0 0 14 14"><path d="M1 7 L13 1 L9 13 L7 8 Z" fill="var(--olive)"/></svg>
        hello@brightpathkids.org
      </span>
      <span class="contact-item">
        <svg class="contact-icon" viewBox="0 0 14 14"><circle cx="7" cy="7" r="7" fill="var(--olive)"/></svg>
        Crestwood Lantern Youth House
      </span>
      <span class="contact-item">
        <svg class="contact-icon" viewBox="0 0 14 14"><circle cx="7" cy="7" r="6" fill="none" stroke="var(--olive)" stroke-width="1.4"/><ellipse cx="7" cy="7" rx="2.6" ry="6" fill="none" stroke="var(--olive)" stroke-width="1.2"/><line x1="1" y1="7" x2="13" y2="7" stroke="var(--olive)" stroke-width="1.2"/></svg>
        www.brightpathkids.org
      </span>
    </div>
  </section>

  <section class="card card--back">
    <div class="stamp-box" aria-label="Stamp area"></div>
    <div class="appeal">
      <p>Copy for End of the Year Flyer</p>
      <p>We need your help to finish out 2018 strong!&nbsp; We have<br>had a wonderful 25th year of serving the children<br>and families of Pasadena here at Crestwood<br>Lantern Youth House with high quality afterschool<br>programs.&nbsp; Hundreds and hundreds of students have<br>been a part of the Bright Path Kids Club family.&nbsp; Our<br>annual budget is $275,000 and we count on $100,000<br>from individual donors.&nbsp; Will you join with us for an<br>end of the year contribution?&nbsp; Remember, you can<br>give online through GivePort.</p>
      <p>Just look for the link on<br>our website - www.brightpathkids.org.</p>
      <p>Merry Christmas from all of us at CLYH!</p>
    </div>
    <address class="return-address">
      Crestwood Lantern Youth House<br>214 N. Alder Grove Ave.<br>Pasadena, CA&nbsp; 91106<br>(626) 555-0142
    </address>
    <div class="label-space" aria-label="Mailing label area"></div>
  </section>

  <span class="side-label" style="left:341px">Front Side</span>
  <span class="side-label" style="left:848px">Back Side</span>
</main>
</body>
</html>
```